Building company buisness cards

We are looking for a sharp modern new look for our business cards.We are a New Zealand based company that specialises in house and land packages.We have attached a photo of the current logo and would like to see if it can be improved somehow if needed.We are open to any colours but we have chosen Black and White at this stage. Feel free to change the font and make the logo smarter looking.Play with the colours and see what looks best.We want a card that looks so good know one will want to throw it away!

Target Market(s)

Building profesonals, home buyers

Industry/Entity Type

Building

Contact Information for Business Card

Derek Haskins
0274930268
derekh@stonerange.co.nz

Font styles to use
Serif
Sans Serif

Colors

Designer to choose colors to be used in the design.

Requirements
Must have
• Just the logo on one side and details on the other
• Clean simple looking card
Nice to have
• Round corners and detail like raised or spot UV
• Something that stands out
Should not have
• To title needed, Director etc

```html
<!DOCTYPE html>
<html lang="en">
<head>
<meta charset="utf-8">
<title>Stonerange Business Card</title>
<link rel="stylesheet" href="https://fonts.googleapis.com/css2?family=Source+Sans+3:wght@400;600;700&display=swap">
<style>
  :root {
    --page-bg: #e9e6e1;
    --card-black: #070707;
    --card-edge: #1c1c1c;
    --frost-top: #eef2f6;
    --frost-mid: #d9dde2;
    --frost-low: #e6cfd3;
    --frost-ring: rgba(255, 255, 255, 0.55);
    --logo-ink: #1e1e1e;
    --name-ink: #b7aa93;
    --detail-ink: #a29b8f;
    --icon-ink: #d8d2c6;
  }
  * { margin: 0; padding: 0; box-sizing: border-box; }
  html, body {
    width: 1200px;
    height: 1120px;
    overflow: hidden;
    background: var(--page-bg);
    font-family: "Source Sans 3", "Myriad Pro", sans-serif;
  }
  .card {
    position: absolute;
    left: 100px;
    top: 274px;
    width: 1000px;
    height: 572px;
    border-radius: 30px;
    overflow: hidden;
    background: linear-gradient(115deg, var(--card-edge) 0%, var(--card-black) 45%, #111 100%);
    box-shadow: 0 20px 50px rgba(0, 0, 0, 0.25);
  }
  .frost-disc {
    position: absolute;
    left: 2px;
    top: -8px;
    width: 576px;
    height: 576px;
    border-radius: 50%;
    background: linear-gradient(180deg, var(--frost-top) 0%, var(--frost-mid) 55%, var(--frost-low) 85%, #d8cdd0 100%);
    border: 20px solid var(--frost-ring);
    background-clip: padding-box;
    box-shadow: 0 0 0 2px rgba(255, 255, 255, 0.25);
  }
  .brand {
    position: absolute;
    left: 0;
    top: 0;
    width: 100%;
    height: 100%;
    display: flex;
    align-items: center;
    justify-content: center;
    gap: 14px;
  }
  .brand-name {
    font-weight: 700;
    font-size: 64px;
    letter-spacing: -0.5px;
    color: var(--logo-ink);
  }
  .brand-dot {
    width: 44px;
    height: 44px;
    border-radius: 50%;
    border: 4px solid var(--logo-ink);
  }
  .details {
    position: absolute;
    right: 54px;
    top: 352px;
    text-align: right;
  }
  .person-name {
    font-weight: 600;
    font-size: 31px;
    color: var(--name-ink);
    margin-bottom: 22px;
    letter-spacing: 0.3px;
  }
  .contact-list { list-style: none; }
  .contact-item {
    display: flex;
    justify-content: flex-end;
    align-items: center;
    gap: 18px;
    font-size: 23px;
    line-height: 35px;
    color: var(--detail-ink);
    letter-spacing: 0.3px;
  }
  .contact-icon {
    width: 22px;
    height: 22px;
    fill: var(--icon-ink);
    flex: none;
  }
</style>
</head>
<body>
  <div class="card">
    <div class="frost-disc">
      <div class="brand">
        <span class="brand-name">Stonerange</span>
        <span class="brand-dot"></span>
      </div>
    </div>

    <div class="details">
      <p class="person-name">Derek Haskins</p>
      <ul class="contact-list">
        <li class="contact-item">
          <span>0274930268</span>
          <svg class="contact-icon" viewBox="0 0 24 24" aria-hidden="true">
            <path d="M2 8c0-2 4-4 10-4s10 2 10 4v2h-5V8c-1-.6-3-1-5-1s-4 .4-5 1v2H2z"/>
            <path d="M6 11h12l2 9H4z M12 13a3 3 0 1 0 0 6a3 3 0 0 0 0-6z" fill-rule="evenodd"/>
          </svg>
        </li>
        <li class="contact-item">
          <span>derekh@stonerange.co.nz</span>
          <svg class="contact-icon" viewBox="0 0 24 24" aria-hidden="true">
            <path d="M2 6h20v1l-10 6L2 7z"/>
            <path d="M2 9l10 6 10-6v10H2z"/>
          </svg>
        </li>
        <li class="contact-item">
          <span>www.stonerange.co.nz</span>
          <svg class="contact-icon" viewBox="0 0 24 24" aria-hidden="true">
            <circle cx="12" cy="12" r="10"/>
            <path d="M8 6c2 1 3 3 1 5s1 4 3 5-1 4-3 3M15 5c-1 2 1 3 3 3M16 13c2 0 3 2 2 4" stroke="#1a1a1a" stroke-width="1.6" fill="none"/>
          </svg>
        </li>
      </ul>
    </div>
  </div>
</body>
</html>
```